Business Card Design

my company buys cars,boats and caravans off the public, and also assists the public in helping them sell there item(brokering),i have an idea of a logo which is.....T$A....THE S BEING A LARGE DOLLAR SIGN,centred. And underneath my business name....TRADER-HOLDER-AGENT,i like black backgrounds, CLEAN SHARP AND TO THE POINT!!

Industry/Entity Type

Business

Contact Information for Business Card

$wap NOWLY.........buyer,seller,broker......cars,boats,caravans...........0427591846.......-swapnowly@traderholderagent.com.au, lmct-58417

Requirements
Must have
• MOBILE NUMBER-0427591846
EMAIL-swapnowly@traderholderagent.com.au
business name-TRADER-HOLDER-AGENT
lmct-58417
what we deal in-Cars,Caravans,Boats
cash,bank chq, finance paid out
Nice to have
• clever logo created by you guys

```html
<!DOCTYPE html>
<html lang="en">
<head>
<meta charset="utf-8">
<title>TRADER-HOLDER-AGENT — Business Card</title>
<link href="https://fonts.googleapis.com/css2?family=Cinzel:wght@500&family=Open+Sans:wght@400&display=swap" rel="stylesheet">
<style>
  :root {
    --page-bg: #3a2e22;
    --card-black: #0b0b0b;
    --card-black-soft: #1c1c1c;
    --gold: #d9b266;
    --gold-light: #f1d99a;
    --gold-deep: #9c7430;
    --ink-light: #e6e6e6;
    --band-ink: #2b210f;
  }
  * { margin: 0; padding: 0; box-sizing: border-box; }
  html, body {
    width: 1200px;
    height: 1023px;
    overflow: hidden;
    background: var(--page-bg);
  }
  .canvas {
    position: relative;
    width: 1200px;
    height: 1023px;
    display: flex;
    align-items: center;
    justify-content: center;
  }
  .card {
    position: relative;
    width: 1000px;
    height: 570px;
    border-radius: 26px;
    overflow: hidden;
    background: linear-gradient(160deg, var(--card-black-soft) 0%, var(--card-black) 55%, #050505 100%);
    box-shadow: 0 20px 50px rgba(0, 0, 0, 0.5);
  }
  .brand {
    position: absolute;
    left: 0;
    right: 0;
    top: 0;
    height: 240px;
    display: flex;
    align-items: center;
    justify-content: center;
    gap: 22px;
  }
  .brand-dot {
    width: 22px;
    height: 22px;
    border-radius: 50%;
    background: var(--gold);
    flex: none;
  }
  .brand-name {
    color: var(--gold);
    font-family: "Cinzel", serif;
    font-weight: 500;
    font-size: 46px;
    letter-spacing: 1px;
    line-height: 1;
  }
  .divider {
    position: absolute;
    left: 0;
    right: 0;
    top: 240px;
    height: 2px;
    background: linear-gradient(90deg, transparent 0%, var(--gold-deep) 12%, var(--gold) 50%, var(--gold-deep) 88%, transparent 100%);
  }
  .details {
    position: absolute;
    left: 0;
    right: 0;
    top: 264px;
    text-align: center;
  }
  .trades {
    color: var(--gold);
    font-family: "Cinzel", serif;
    font-weight: 500;
    font-size: 31px;
    line-height: 1;
    margin-bottom: 28px;
  }
  .contact-line {
    color: var(--ink-light);
    font-family: "Open Sans", sans-serif;
    font-size: 24px;
    line-height: 38px;
  }
  .payment-band {
    position: absolute;
    left: 0;
    right: 0;
    bottom: 0;
    height: 78px;
    display: flex;
    align-items: center;
    justify-content: center;
    background: linear-gradient(180deg, var(--gold-light) 0%, var(--gold) 40%, var(--gold-deep) 100%);
    color: var(--band-ink);
    font-family: "Open Sans", sans-serif;
    font-size: 23px;
    letter-spacing: 1px;
  }
  .payment-band .sep { margin: 0 14px; }
</style>
</head>
<body>
  <main class="canvas">
    <section class="card" aria-label="Business card front">
      <header class="brand">
        <span class="brand-dot"></span>
        <h1 class="brand-name">TRADER-HOLDER-AGENT</h1>
      </header>
      <div class="divider"></div>
      <div class="details">
        <p class="trades">CARS-BOATS-CARAVANS</p>
        <p class="contact-line">0427591846</p>
        <p class="contact-line">swapnowly@traderholderagent.com.au</p>
        <p class="contact-line">LMCT-58417</p>
      </div>
      <footer class="payment-band">
        CASH<span class="sep">|</span>BANK CHQ<span class="sep">|</span>FINANCE PAID OUT
      </footer>
    </section>
  </main>
</body>
</html>
```